quality electrical business needs a logo design

we need a logo design for our new company starting up. I'm a sole trader electrician. I want to make the VES prominent in Vellar Electrical Services. Information I would want on the business card would be;
Business Name: Vellar Electrical Services
What I do: Domestic/Commercial/Industrial Installation & Maintenance
Email Address: Brenton.vellar@qorvamail.net.au
Contact no: Brenton 0438261574
Electrical License no: EC47391

Open to different Colours but would like to see some with Navy blue. I want to promote professionalism and have a modern feel about it.

```html
<!DOCTYPE html>
<html lang="en">
<head>
<meta charset="utf-8">
<title>Vellar Electrical Services – Business Card</title>
<link href="https://fonts.googleapis.com/css2?family=Arimo:wght@700&family=Didact+Gothic&display=swap" rel="stylesheet">
<style>
  :root {
    --page-bg: #f2f2f2;
    --card-bg: #262626;
    --brand-blue: #2f4fa3;
    --band-text: #72b6e4;
    --text-light: #ffffff;
    --watermark: #2f2f31;
  }
  * { box-sizing: border-box; margin: 0; padding: 0; }
  html, body {
    width: 1200px;
    height: 1000px;
    overflow: hidden;
    background: var(--page-bg);
  }
  .canvas {
    position: relative;
    width: 1200px;
    height: 1000px;
  }
  .business-card {
    position: absolute;
    left: 350px;
    top: 100px;
    width: 500px;
    height: 800px;
    background: var(--card-bg);
    overflow: hidden;
  }
  .brand {
    position: absolute;
    left: 50px;
    top: 150px;
    display: flex;
    align-items: center;
    gap: 16px;
  }
  .brand-square {
    width: 22px;
    height: 22px;
    background: var(--brand-blue);
    flex: none;
  }
  .brand-name {
    font-family: "Arimo", Arial, sans-serif;
    font-weight: 700;
    font-size: 31px;
    line-height: 1.15;
    color: var(--brand-blue);
    letter-spacing: 0.5px;
  }
  .contact {
    position: absolute;
    left: 70px;
    top: 395px;
    color: var(--text-light);
    font-family: "Didact Gothic", "Century Gothic", sans-serif;
    font-size: 22px;
  }
  .contact-name {
    font-family: "Arimo", Arial, sans-serif;
    font-weight: 700;
    font-size: 23px;
    margin-bottom: 16px;
  }
  .contact-line {
    display: flex;
    align-items: center;
    gap: 10px;
    height: 32px;
  }
  .contact-icon {
    width: 24px;
    height: 20px;
    flex: none;
  }
  .watermark {
    position: absolute;
    left: 40px;
    top: 545px;
    font-family: "Arimo", Arial, sans-serif;
    font-weight: 700;
    font-size: 150px;
    letter-spacing: 20px;
    color: var(--watermark);
    line-height: 1;
  }
  .services-band {
    position: absolute;
    left: 0;
    top: 665px;
    width: 100%;
    height: 92px;
    background: var(--brand-blue);
    display: flex;
    flex-direction: column;
    justify-content: center;
    align-items: center;
    font-family: "Didact Gothic", "Century Gothic", sans-serif;
    font-size: 22px;
    line-height: 1.2;
    color: var(--band-text);
    text-align: center;
  }
</style>
</head>
<body>
<main class="canvas">
  <section class="business-card">
    <div class="brand">
      <span class="brand-square"></span>
      <span class="brand-name">Vellar Electrical<br>Services</span>
    </div>

    <div class="contact">
      <p class="contact-name">Brenton</p>
      <p class="contact-line">
        <svg class="contact-icon" viewBox="0 0 24 20" aria-hidden="true">
          <path d="M2 7c0-3 4-5 10-5s10 2 10 5l-1 2-4-1V6c-3-1-7-1-10 0v2L3 9z" fill="#fff"/>
          <path d="M7 10h10l3 8H4z" fill="#fff"/>
          <circle cx="12" cy="14" r="2.2" fill="#262626"/>
        </svg>
        <span>0438261574</span>
      </p>
      <p class="contact-line">
        <svg class="contact-icon" viewBox="0 0 24 20" aria-hidden="true">
          <rect x="2" y="3" width="20" height="14" fill="#fff"/>
          <path d="M2 3l10 8 10-8" fill="none" stroke="#262626" stroke-width="1.6"/>
        </svg>
        <span>Brenton.vellar@qorvamail.net.au</span>
      </p>
      <p class="contact-line">Electrical License no: EC47391</p>
    </div>

    <div class="watermark" aria-hidden="true">VES</div>

    <div class="services-band">
      <span>Domestic/Commercial/Industrial</span>
      <span>Installation &amp; Maintenance</span>
    </div>
  </section>
</main>
</body>
</html>
```